New Company Business Card Design

I have a new company logo and I want a new business card design. I dont know if the logo file i attached is in the correct format or quality. We are a New York City Specialty construction Firm specializing in high risk out of the box projects. I want a simple and classy business card that people will his card is as crisp as the work his company does.

Target Market(s)

Clients in the heavy construction industry in New York City

Industry/Entity Type

Construction Company

Contact Information for Business Card

Simple Classy - DIFFERENT

Font styles to use
Other font styles liked:
• Mach the logo font in some way

Colors

Designer to choose colors to be used in the design.

Requirements
Must have
• Uniqueness
Nice to have
• Nothing particular - Just different and classy - Timeless
Should not have
• Goofy Shit or Gimmicky shit

```html
<!DOCTYPE html>
<html lang="en">
<head>
<meta charset="utf-8">
<title>Korvan Builders, Inc. — Business Card</title>
<link rel="stylesheet" href="https://fonts.googleapis.com/css2?family=Open+Sans:wght@400;600;700&display=swap">
<style>
  :root {
    --bg: #e4e4e6;
    --card-white: #ffffff;
    --brand-blue: #0a6fc2;
    --blue-light: #05a9e6;
    --blue-deep: #0b4f93;
    --ink: #1b1b1b;
    --divider: #c9c9cc;
  }
  * { box-sizing: border-box; margin: 0; padding: 0; }
  html, body { width: 1200px; height: 864px; overflow: hidden; }
  body {
    background: var(--bg);
    font-family: "Open Sans", Arial, sans-serif;
    position: relative;
  }
  .card {
    position: absolute;
    width: 540px;
    height: 309px;
    border-radius: 4px;
    box-shadow: 0 10px 28px rgba(0,0,0,0.18);
    overflow: hidden;
  }
  .card--back {
    left: 600px;
    top: 90px;
    background: linear-gradient(180deg, var(--blue-light) 0%, var(--brand-blue) 55%, var(--blue-deep) 100%);
    display: flex;
    align-items: center;
    justify-content: center;
  }
  .card--front {
    left: 60px;
    top: 460px;
    background: var(--card-white);
  }
  .wordmark {
    display: flex;
    align-items: center;
    gap: 12px;
    font-weight: 700;
    letter-spacing: 0.04em;
    text-transform: uppercase;
    line-height: 1.05;
    white-space: nowrap;
  }
  .wordmark__square { width: 22px; height: 22px; flex: none; }
  .card--back .wordmark { color: #ffffff; font-size: 34px; }
  .card--back .wordmark__square { background: #ffffff; }
  .card--front .wordmark {
    position: absolute;
    left: 30px;
    top: 118px;
    color: var(--brand-blue);
    font-size: 23px;
  }
  .card--front .wordmark__square { background: var(--brand-blue); }
  .divider {
    position: absolute;
    left: 298px;
    top: 30px;
    width: 40px;
    height: 250px;
  }
  .contact {
    position: absolute;
    left: 346px;
    top: 80px;
  }
  .contact__name {
    color: var(--brand-blue);
    font-size: 18px;
    font-weight: 400;
    letter-spacing: 0.02em;
    text-transform: uppercase;
    line-height: 1.1;
    white-space: nowrap;
  }
  .contact__title {
    color: var(--ink);
    font-size: 14px;
    margin-bottom: 24px;
  }
  .contact__list { list-style: none; }
  .contact__item {
    display: flex;
    align-items: center;
    gap: 9px;
    font-size: 14px;
    color: var(--ink);
    line-height: 1.5;
    white-space: nowrap;
  }
  .contact__icon { width: 14px; height: 14px; flex: none; }
</style>
</head>
<body>

  <section class="card card--back" aria-label="Card back">
    <div class="wordmark">
      <span class="wordmark__square"></span>
      <span>Korvan<br>Builders, Inc.</span>
    </div>
  </section>

  <section class="card card--front" aria-label="Card front">
    <div class="wordmark">
      <span class="wordmark__square"></span>
      <span>Korvan<br>Builders, Inc.</span>
    </div>

    <svg class="divider" viewBox="0 0 40 250" aria-hidden="true">
      <path d="M36 0 C 8 70, 6 170, 4 250" fill="none" stroke="var(--divider)" stroke-width="1.5"/>
    </svg>

    <div class="contact">
      <p class="contact__name">Daniel Reyes</p>
      <p class="contact__title">Manager</p>
      <ul class="contact__list">
        <li class="contact__item">
          <svg class="contact__icon" viewBox="0 0 14 14" aria-hidden="true">
            <rect width="14" height="14" rx="2" fill="var(--brand-blue)"/>
            <rect x="4.5" y="2.5" width="5" height="9" rx="1" fill="none" stroke="#fff" stroke-width="1.2"/>
          </svg>
          <span>+01 555 014 372</span>
        </li>
        <li class="contact__item">
          <svg class="contact__icon" viewBox="0 0 14 14" aria-hidden="true">
            <rect width="14" height="14" rx="2" fill="var(--brand-blue)"/>
            <path d="M4 3 L6 3 L6.8 5.2 L5.6 6.2 C6.3 7.6 7 8.3 8 8.6 L9 7.5 L11 8.3 L11 10.3 C7 10.6 3.6 7 4 3 Z" fill="#fff"/>
          </svg>
          <span>+01 555 014 372</span>
        </li>
        <li class="contact__item">
          <svg class="contact__icon" viewBox="0 0 14 14" aria-hidden="true">
            <rect width="14" height="14" rx="2" fill="var(--brand-blue)"/>
            <rect x="2.5" y="4" width="9" height="6.5" fill="none" stroke="#fff" stroke-width="1.1"/>
            <path d="M2.5 4 L7 7.8 L11.5 4" fill="none" stroke="#fff" stroke-width="1.1"/>
          </svg>
          <span>info@korvanbuild.com</span>
        </li>
        <li class="contact__item">
          <svg class="contact__icon" viewBox="0 0 14 14" aria-hidden="true">
            <rect width="14" height="14" rx="2" fill="var(--brand-blue)"/>
            <circle cx="7" cy="7" r="4.2" fill="none" stroke="#fff" stroke-width="1.1"/>
            <path d="M2.8 7 H11.2 M7 2.8 C5 5 5 9 7 11.2 M7 2.8 C9 5 9 9 7 11.2" fill="none" stroke="#fff" stroke-width="0.9"/>
          </svg>
          <span>www.korvanbuild.com</span>
        </li>
      </ul>
    </div>
  </section>

</body>
</html>
```